Label Design for Nuts package*

Develop the design for a label for nuts sold in a paperbag.

you can find our website here: www.kornfeld-snack.de.
Here comes the link to our catalogue: https://www.blattwerk-docs.com/de/document/read/48172956/kornfeld-premium-snacks-gesamtkatalog-2019

With this product we are targeting private customers who want to buy nuts with plastic free packaging online.
The colours of the label should fit the brown paper bag.

```html
<!DOCTYPE html>
<html lang="en">
<head>
<meta charset="utf-8">
<title>Kornfeld Premium Almonds – Label</title>
<link href="https://fonts.googleapis.com/css2?family=Open+Sans:wght@400;600;700&family=Ultra&display=swap" rel="stylesheet">
<style>
  :root {
    --backdrop: #c49a86;
    --band: #34191a;
    --ink: #3b1d1b;
    --wood-light: #efe6bf;
    --wood-mid: #e4d6a2;
    --wood-edge: #d8c48a;
    --almond-light: #c98f5a;
    --almond-dark: #8a5128;
    --label-text-light: #f3ead8;
  }
  * { margin: 0; padding: 0; box-sizing: border-box; }
  html, body {
    width: 1200px; height: 834px; overflow: hidden;
    background: var(--backdrop);
  }
  .canvas {
    position: relative; width: 1200px; height: 834px;
  }
  .label {
    position: absolute; left: 395px; top: 34px;
    width: 410px; height: 766px;
    background: var(--band);
    border-radius: 10px 10px 4px 4px;
    overflow: hidden;
  }
  .label__top-band {
    position: absolute; left: 0; top: 0; width: 100%; height: 132px;
    background: var(--band);
  }
  .label__seal-line {
    position: absolute; left: 0; width: 100%; height: 2px;
    background: rgba(255,255,255,0.08);
  }
  .label__panel {
    position: absolute; left: 0; top: 132px; width: 100%; height: 534px;
    background:
      linear-gradient(90deg, var(--wood-edge) 0%, var(--wood-light) 14%, var(--wood-mid) 50%, var(--wood-light) 86%, var(--wood-edge) 100%);
    border-top: 3px solid var(--wood-edge);
  }
  .brand {
    position: absolute; left: 0; top: 22px; width: 100%;
    text-align: center; color: var(--ink);
  }
  .brand__mark {
    display: block; width: 26px; height: 26px; margin: 0 auto 8px;
    border-radius: 50%; background: var(--ink);
  }
  .brand__name {
    font-family: "Open Sans", sans-serif; font-weight: 400;
    font-size: 30px; letter-spacing: 1px; line-height: 1;
  }
  .brand__tagline {
    display: inline-block; margin-top: 4px; padding: 0 4px 2px;
    font-family: "Open Sans", sans-serif; font-weight: 700;
    font-size: 8px; letter-spacing: 1.5px;
    border-bottom: 1px solid var(--ink);
  }
  .title {
    position: absolute; left: 0; top: 128px; width: 100%; height: 180px;
  }
  .title text { fill: var(--ink); }
  .title__eyebrow { font-family: "Open Sans", sans-serif; font-weight: 700; font-size: 22px; }
  .title__product { font-family: "Ultra", serif; font-size: 54px; letter-spacing: 1px; }
  .claim {
    position: absolute; left: 0; top: 312px; width: 100%;
    text-align: center; color: var(--ink);
    font-family: "Open Sans", sans-serif; font-weight: 600; font-size: 15px;
    transform: rotate(-1.5deg);
  }
  .product-photo {
    position: absolute; right: 6px; bottom: 0; width: 250px; height: 190px;
    border-radius: 50% 45% 0 0 / 60% 55% 0 0;
    background: radial-gradient(ellipse at 55% 45%, var(--almond-light) 0%, var(--almond-dark) 70%, rgba(138,81,40,0) 100%);
  }
  .label__bottom-band {
    position: absolute; left: 0; bottom: 0; width: 100%; height: 100px;
    background: var(--band);
  }
  .net-weight {
    position: absolute; right: 30px; top: 22px;
    font-family: "Open Sans", sans-serif; font-weight: 600; font-size: 17px;
    color: var(--label-text-light);
    transform: rotate(-4deg);
  }
</style>
</head>
<body>
<main class="canvas">
  <section class="label">
    <div class="label__top-band">
      <span class="label__seal-line" style="top:46px"></span>
      <span class="label__seal-line" style="top:72px"></span>
      <span class="label__seal-line" style="top:98px"></span>
    </div>

    <div class="label__panel">
      <div class="brand">
        <span class="brand__mark"></span>
        <div class="brand__name">kornfeld</div>
        <div class="brand__tagline">PREMIUM SNACKS</div>
      </div>

      <svg class="title" viewBox="0 0 410 180" aria-label="Premium Almonds">
        <defs>
          <path id="arc-eyebrow" d="M130 42 Q205 22 280 42"/>
          <path id="arc-product" d="M18 132 Q205 50 392 132"/>
        </defs>
        <text class="title__eyebrow" text-anchor="middle">
          <textPath href="#arc-eyebrow" startOffset="50%">PREMIUM</textPath>
        </text>
        <text class="title__product" text-anchor="middle">
          <textPath href="#arc-product" startOffset="50%">ALMONDS</textPath>
        </text>
      </svg>

      <p class="claim">Crunchy , Nutritious &amp; Healthy</p>

      <div class="product-photo" role="img" aria-label="Photo of a heap of whole shelled almonds"></div>
    </div>

    <div class="label__bottom-band">
      <p class="net-weight">Net. wt. 300gm</p>
    </div>
  </section>
</main>
</body>
</html>
```